Style with Kindness needs a new flyer fast for a giveaway

I am running a contest for the month of December. The woman selected as the winner of the contest will be someone that that has survived a domestic violence situation but would like to kick start in her new life journey. The winner selected will receive 1 month free personal training with a fitness coach 3 times a week, 4 week delivery of smoothies from Leafwhirler and a style consultation and outfit by Celebrity Stylist R.Tasker. All interested candidates should submit a brief personal bio including the reason they should be selected. Submissions are due December 24th and the winner will be selected December 31. Submissions should be sent to stylewithkindnessdallas@mailbox-example.net

Industry/Entity Type

Fashion

Font styles to use
Serif

Colors
886aae
b7a5cd
e4daeb
d2a4cc
b768aa
a64599
e34197
e667a6
eea4c8

Requirements
Must have
• The project has to be worded in a stylish way. I want it is be creative and eye catchy. It also needs to have my style with kindness logo and my Ava P logo on the flyer that I will attach to the brief
Nice to have
• I would like to see different fonts to break up the flyer
Should not have
• It should not just be a paragraph of what I already typed about the contest

```html
<!DOCTYPE html>
<html lang="en">
<head>
<meta charset="utf-8">
<title>Style with Kindness – December Giveaway</title>
<link rel="stylesheet" href="https://fonts.googleapis.com/css2?family=Comfortaa:wght@300&family=Montserrat:wght@400;600;700&family=Playball&family=Playfair+Display:ital,wght@1,400;1,700;1,900&display=swap">
<style>
:root{
  --violet:#886aae;
  --lilac:#b7a5cd;
  --mist:#e4daeb;
  --rose:#d2a4cc;
  --orchid:#b768aa;
  --plum:#a64599;
  --deep:#5a2d82;
  --night:#3e1f52;
  --pale-text:#cdbfe0;
  --white:#ffffff;
}
*{margin:0;padding:0;box-sizing:border-box}
html,body{width:849px;height:1200px;overflow:hidden;background:var(--white)}
.flyer{position:relative;width:849px;height:1200px;overflow:hidden;font-family:'Montserrat',sans-serif}
.backdrop{position:absolute;inset:0}
.abs{position:absolute}

.hand-art{left:532px;top:0;width:133px;height:193px;border-radius:0 0 66px 66px;
  background:linear-gradient(180deg,rgba(244,244,246,.95),rgba(220,221,227,.75))}
.title-lead{left:89px;top:26px;font-family:'Playfair Display',serif;font-style:italic;font-weight:700;
  font-size:48px;color:var(--white);white-space:nowrap;transform:scaleX(.9);transform-origin:left top}
.title-word{font-family:'Playfair Display',serif;font-style:italic;font-weight:900;color:var(--deep);
  font-size:125px;line-height:1;transform:scaleX(.66);transform-origin:left top;letter-spacing:-2px;white-space:nowrap}
.title-word.one{left:85px;top:75px}
.title-word.two{left:298px;top:170px}

.ribbons{left:72px;top:280px;width:245px;height:170px}
.ribbon-text{font-family:'Playball',cursive;fill:var(--white)}

.work-lead{left:486px;top:316px;font-family:'Comfortaa',sans-serif;font-weight:300;color:var(--white);font-size:40px}
.work-main{left:484px;top:360px;font-family:'Comfortaa',sans-serif;font-weight:300;color:var(--white);font-size:60px}
.contest-line{left:486px;top:444px;font-weight:600;color:var(--pale-text);font-size:25px;line-height:34px}

.winner-head{font-family:'Playfair Display',serif;font-style:italic;font-weight:400;color:var(--violet);font-size:27px}
.winner-head.a{left:32px;top:526px}
.winner-head.b{left:188px;top:560px}

.prize-bar{height:55px;border-radius:0 40px 40px 0;
  background:linear-gradient(90deg,var(--plum),var(--orchid));color:var(--white);
  font-weight:600;font-size:15.5px;line-height:20px;display:flex;align-items:center;white-space:nowrap}
.prize-icon{width:88px;height:88px;border-radius:50%;background:var(--white);border:5px solid var(--plum);
  display:flex;align-items:center;justify-content:center}
.p1.prize-bar{left:105px;top:612px;width:358px;padding-left:57px}
.p1.prize-icon{left:63px;top:595px}
.p2.prize-bar{left:197px;top:697px;width:351px;padding-left:51px}
.p2.prize-icon{left:151px;top:681px}
.p3.prize-bar{left:282px;top:783px;width:353px;padding-left:53px}
.p3.prize-icon{left:238px;top:766px}

.apply{left:0;top:872px;width:508px;text-align:center;color:var(--deep);font-weight:600;font-size:18.5px;line-height:23px}
.rule{left:28px;top:926px;width:451px;border-top:1.5px dotted var(--deep)}
.send{left:0;top:932px;width:508px;text-align:center;color:var(--plum);font-size:14px;line-height:20px}
.send strong{font-weight:700;font-size:13px}

.date-box{height:48px;width:214px;border-radius:8px;background:var(--lilac);color:var(--white);
  font-size:14px;line-height:19px;display:flex;align-items:center;padding-left:24px}
.d1.date-box{left:24px;top:993px}
.d2.date-box{left:268px;top:993px;padding-left:12px}
.cal{width:59px;height:68px;background:var(--white);border-radius:4px;box-shadow:0 3px 5px rgba(0,0,0,.2);overflow:hidden;text-align:center}
.cal-month{background:var(--plum);color:var(--white);font-weight:600;font-size:12px;height:20px;line-height:20px}
.cal-day{color:#333;font-weight:700;font-size:28px;line-height:46px}
.c1{left:168px;top:984px}
.c2{left:412px;top:984px}

.sponsor-band{left:0;top:1066px;width:849px;height:134px;background:var(--white)}
.sponsor-label{left:0;top:1078px;width:490px;text-align:center;font-size:14.5px;color:#111}
.brand{font-family:'Montserrat',sans-serif;font-weight:600;color:var(--deep);white-space:nowrap}
.brand.kind{left:40px;top:1137px;font-size:16px}
.brand.ava{left:282px;top:1128px;font-size:30px}
.divider{left:241px;top:1106px;width:2px;height:84px;background:var(--plum)}

.gown-art{left:515px;top:870px;width:315px;height:306px;border-radius:45% 45% 40% 40%/30% 30% 70% 70%;
  background:radial-gradient(ellipse at 55% 65%,rgba(166,69,153,.85),rgba(210,164,204,.6) 55%,rgba(228,218,235,0) 80%)}
</style>
</head>
<body>
<main class="flyer">
  <svg class="backdrop" width="849" height="1200" viewBox="0 0 849 1200" aria-hidden="true">
    <defs>
      <linearGradient id="sky" x1="0" y1="0" x2="1" y2="0">
        <stop offset="0" stop-color="#c2b3d9"/><stop offset="1" stop-color="#9483bf"/>
      </linearGradient>
      <linearGradient id="wedge" x1="0" y1="0" x2="1" y2="0">
        <stop offset="0" stop-color="#7d58a6"/><stop offset="1" stop-color="#3e1f52"/>
      </linearGradient>
      <linearGradient id="floor" x1="0" y1="0" x2="1" y2="0">
        <stop offset="0" stop-color="#f2eef6"/><stop offset="1" stop-color="#c4b3da"/>
      </linearGradient>
      <linearGradient id="crowd" x1="0" y1="0" x2="1" y2="0">
        <stop offset="0" stop-color="#d77bb7"/><stop offset=".35" stop-color="#c7a1d2"/>
        <stop offset=".6" stop-color="#9a92bf"/><stop offset=".8" stop-color="#e5a4cb"/>
        <stop offset="1" stop-color="#b7a5cd"/>
      </linearGradient>
      <linearGradient id="crowd-fade" x1="0" y1="0" x2="0" y2="1">
        <stop offset="0" stop-color="#fff" stop-opacity="1"/>
        <stop offset="1" stop-color="#fff" stop-opacity=".15"/>
      </linearGradient>
      <mask id="crowd-mask"><rect x="0" y="420" width="849" height="310" fill="url(#crowd-fade)"/></mask>
    </defs>
    <polygon points="0,0 849,0 849,218 0,435" fill="url(#sky)"/>
    <polygon points="0,435 849,218 849,741" fill="url(#wedge)"/>
    <polygon points="0,435 849,741 849,1200 0,1200" fill="url(#floor)"/>
  </svg>

  <svg class="abs" style="left:0;top:0" width="849" height="760" viewBox="0 0 849 760" role="img" aria-label="Illustration of raised fists and one open hand in pink and lilac tones">
    <polygon points="165,462 400,430 781,594 781,717 165,495" fill="url(#crowd)" opacity=".8" mask="url(#crowd-mask)"/>
  </svg>

  <div class="abs hand-art" role="img" aria-label="Illustration of an open white hand reaching down"></div>

  <h1>
    <span class="abs title-lead">are you survived from</span>
    <span class="abs title-word one">domestic</span>
    <span class="abs title-word two">violence</span>
  </h1>

  <svg class="abs ribbons" viewBox="0 0 245 170" aria-label="Together we can change our world">
    <polygon points="12,35 218,4 221,44 16,76" fill="#6a3389"/>
    <polygon points="2,80 232,44 236,86 6,122" fill="#9a6ab8"/>
    <polygon points="12,126 200,96 202,134 16,165" fill="#a885c6"/>
    <g transform="rotate(-8 120 85)">
      <text class="ribbon-text" x="62" y="60" font-size="31">Together</text>
      <text class="ribbon-text" x="28" y="103" font-size="31">We can change</text>
      <text class="ribbon-text" x="50" y="145" font-size="31">our world</text>
    </g>
  </svg>

  <p class="abs work-lead">Let’s work</p>
  <p class="abs work-main">together...</p>
  <p class="abs contest-line">Participate a contest<br>to end domestic violence.</p>

  <h2>
    <span class="abs winner-head a">The winner selected</span>
    <span class="abs winner-head b">will receive</span>
  </h2>

  <div class="abs prize-bar p1">1 month free personal training<br>with a fitness coach 3 times a week</div>
  <div class="abs prize-icon p1">
    <svg width="46" height="46" viewBox="0 0 46 46" aria-label="Fitness training">
      <circle cx="23" cy="9" r="6" fill="var(--plum)"/>
      <rect x="4" y="20" width="38" height="5" rx="2" fill="var(--plum)"/>
      <path d="M17 17h12v14H17z" fill="var(--plum)"/>
      <path d="M15 31h6v12h-6zM25 31h6v12h-6z" fill="var(--plum)"/>
    </svg>
  </div>

  <div class="abs prize-bar p2">4 week delivery of smoothies<br>from Leafwhirler</div>
  <div class="abs prize-icon p2">
    <svg width="44" height="48" viewBox="0 0 44 48" aria-label="Smoothie cup">
      <path d="M26 10 L34 1" stroke="var(--plum)" stroke-width="3" stroke-linecap="round"/>
      <rect x="6" y="10" width="32" height="7" rx="2" fill="var(--plum)"/>
      <path d="M9 19h26l-3 26H12z" fill="var(--plum)"/>
      <rect x="10" y="27" width="24" height="6" fill="var(--white)"/>
    </svg>
  </div>

  <div class="abs prize-bar p3">A style consultation and outfit by<br>Celebrity Stylist R.Tasker</div>
  <div class="abs prize-icon p3">
    <svg width="40" height="50" viewBox="0 0 40 50" aria-label="Dress">
      <path d="M14 2 L14 10 L10 20 L2 46 H38 L30 20 L26 10 L26 2 L22 8 H18 Z" fill="var(--plum)"/>
      <rect x="10" y="18" width="20" height="3" fill="var(--white)"/>
    </svg>
  </div>

  <p class="abs apply">All interested should submit a brief personal bio<br>including the reason why you should be selected.</p>
  <div class="abs rule"></div>
  <p class="abs send">Your Submissions should be emailed to<br><strong>stylewithkindnessdallas@mailbox-example.net</strong></p>

  <div class="abs date-box d1">Last Date of<br>Submission</div>
  <div class="abs cal c1"><div class="cal-month">DEC</div><div class="cal-day">24</div></div>
  <div class="abs date-box d2">Date of<br>Winner Selection</div>
  <div class="abs cal c2"><div class="cal-month">DEC</div><div class="cal-day">31</div></div>

  <div class="abs sponsor-band"></div>
  <p class="abs sponsor-label">Event Sponsored by :</p>
  <p class="abs brand kind">Style with Kindness</p>
  <div class="abs divider"></div>
  <p class="abs brand ava">Ava P</p>

  <div class="abs gown-art" role="img" aria-label="Illustration of a woman in a flowing purple gown"></div>
</main>
</body>
</html>
```